Book cover needed for Christian Non-Fiction Book

I need book cover design (eBook , Paperback, and possibly case laminate Hardcover) for use on Folvane Press and Corvel Print.
Title: Bound for Shore
Sub-Title: Leaving Harbors and Walking in Quiet Trust
Author: Neil Varden
Also on front cover "Forward by R. Leona Pask"

I like clean/simple designs. Below are links to examples of covers I like...
https://www.shelvora.example/dp/Q4821MZT0X?tag=kelvpage-20&linkCode=ogi&th=1&psc=1
https://www.shelvora.example/dp/Q48HTRNWAC?tag=kelvpage-20&linkCode=ogi&th=1&psc=1
https://www.shelvora.example/dp/Q22FKD93XJ?tag=kelvpage-20&linkCode=ogi&th=1&psc=1
https://www.shelvora.example/dp/Q48W3PLMHD?tag=kelvpage-20&linkCode=ogi&th=1&psc=1
https://www.shelvora.example/dp/Q48R5ZZCQN?tag=kelvpage-20&linkCode=ogi&th=1&psc=1
https://www.shelvora.example/dp/Q22H0KKPU7?tag=kelvpage-20&linkCode=ogi&th=1&psc=1

The main idea for Bound for Shore is that God is a sending God and being "on the move" or journeying is central to God's character, and therefore God's people. I write about our hesitancy to "go," and how the Bible is full of stories about people "going" from Abraham to Jesus, to the disciples of Jesus.

The core biblical text is the Great Commission in Matthew 28:16-20, where Jesus sends out his followers, though some of them doubt.

This paragraph from the forward by R. Leona Pask captures the tone of the book well:
This book is a call amid the turmoil. Sacred scripture contains no shortage of narratives in which humans are pulled from their ordinary lives with an inciting incident whose stakes are high. These Biblical figures are lulled from complacency and comfort zones—and yet they are reluctant to serve because they question their ability and influence. Their lessons are relevant for us today: They, and we, are always called and sent with authority. The power of the Holy Spirit equips their “going”—and ours. It’s a sending out that looks less like mastery and more humility. It’s a sending out that is unequivocal service to others modelled in a rabbi-reformer who washed feet and touched the unclean.

I have previously published two shorter books and would be very interested in getting new covers for the old books these so that the three have a similar feel. Whichever designer I go with for "Bound for Shore" I would also want to work with on creating a "branded look" for the other two books.

Target Market(s)

Christian, Religion, Spirituality Readers

Requirements
Must have
• The front cover must have this copy...
Bound for Shore
Leaving Harbors and Walking in Quiet Trust
Neil Varden
Forward by R. Leona Pask

Must be willing to do the full paperback and/or hardcover, but start with thefront cover please
Nice to have
• See attached files for some book covers I like

```html
<!DOCTYPE html>
<html lang="en">
<head>
<meta charset="utf-8">
<title>Bound for Shore — Neil Varden</title>
<link rel="stylesheet" href="https://fonts.googleapis.com/css2?family=Tenor+Sans&display=swap">
<style>
  :root {
    --page: #ffffff;
    --sky-top: #c9d3d6;
    --sky-mid: #b9c9cf;
    --sky-low: #f4f5f4;
    --title-red: #c8141f;
    --ink: #2b2b2b;
    --author-brown: #5a3517;
    --balloon-red: #d4262a;
    --balloon-light: #f2a58a;
  }
  * { margin: 0; padding: 0; box-sizing: border-box; }
  html, body {
    width: 1200px; height: 1200px; overflow: hidden;
    background: var(--page);
  }
  .canvas {
    position: relative; width: 1200px; height: 1200px;
    background: var(--page);
  }
  .cover {
    position: absolute; left: 200px; top: 0;
    width: 800px; height: 1200px; overflow: hidden;
    font-family: "Tenor Sans", "Gill Sans", sans-serif;
    text-align: center;
  }
  .sky {
    position: absolute; inset: 0;
    background: linear-gradient(180deg, var(--sky-top) 0%, var(--sky-mid) 35%, #dfe5e6 58%, var(--sky-low) 72%, #ffffff 100%);
  }
  .balloon {
    position: absolute; left: 282px; top: 0;
    width: 318px; height: 292px;
    border-radius: 0 0 50% 50% / 0 0 40% 40%;
    background: radial-gradient(ellipse at 45% 30%, var(--balloon-light) 0%, var(--balloon-red) 70%);
  }
  .title {
    position: absolute; left: 0; right: 0; top: 392px;
    color: var(--title-red);
    font-size: 114px; line-height: 150px; font-weight: 400;
    letter-spacing: 1px; text-transform: uppercase;
    white-space: nowrap;
  }
  .subtitle {
    position: absolute; left: 0; right: 0; top: 742px;
    color: var(--ink);
    font-size: 28px; line-height: 56px;
    letter-spacing: 3px; text-transform: uppercase;
  }
  .author {
    position: absolute; left: 0; right: 0; top: 980px;
    color: var(--author-brown);
    font-size: 48px; line-height: 60px;
    letter-spacing: 2px; text-transform: uppercase;
  }
  .foreword {
    position: absolute; left: 0; right: 0; top: 1040px;
    color: var(--author-brown);
    font-size: 25px; line-height: 30px;
    letter-spacing: 1.5px; text-transform: uppercase;
  }
</style>
</head>
<body>
<div class="canvas">
  <article class="cover">
    <div class="sky" role="img" aria-label="Soft overcast sky fading from blue-grey clouds to white"></div>
    <div class="balloon" role="img" aria-label="Red and white striped hot air balloon drifting upward"></div>
    <h1 class="title">Bound For<br>Shore</h1>
    <p class="subtitle">Leaving Harbors<br>and Walking in<br>Quiet Trust</p>
    <p class="author">Neil Varden</p>
    <p class="foreword">Forward by R. Leona Pask</p>
  </article>
</div>
</body>
</html>
```